POOL BUILDING CONTRACTOR

our company has shifter focus over the past 18 month we no longer have a retail store and no longer clean pools we build concrete pools. our website if 5 years old we need a completely new site that shows our core product, building concrete pools & renovate concrete pools

here is a few of our competitors;
brantelwaters.com
okvimbuilders.com
ridgeviewlagoonworks.com
plunvora.com
halvertonbasinsandtubs.com
dremblewaterne.com

one we land on a final design I will upload customer before and after photos and any other content needed

Target Market(s)

People looking to build or renovate there pool

Industry/Entity Type

swimming pool

Coding

Coded - Design and coding required

Number of Pages Required

5+ page

Colors
0054AA
0677BA
7BADD7
CADEEF
E8F1F8

Requirements
Must have
• financing Service-Repairs & liners new build-photos renovate-remodeling design-consult customer-reviews Gallery Before-After Contact us 3D Design & Modeling construction process & Timeline Equipment Features Hardscapes I like these sites https://meadowlarkbasinsbycraft.com/ https://holtbergwaters.com/

```html
<!DOCTYPE html>
<html lang="en">
<head>
<meta charset="utf-8">
<title>Tidewell – Concrete Pool Builders</title>
<link href="https://fonts.googleapis.com/css2?family=Nunito:wght@600;700;800&family=Open+Sans:wght@400;600;700&display=swap" rel="stylesheet">
<style>
:root{
  --cyan:#14b4e6;
  --cyan-deep:#0e9fd3;
  --navy:#2f4466;
  --ink:#333a44;
  --muted:#7a7f87;
  --panel:#e7e7e7;
  --charcoal:#3b4047;
  --footer:#3e4e68;
  --white:#ffffff;
  --star:#f5b82e;
}
*{box-sizing:border-box;margin:0;padding:0}
html,body{width:1200px;height:4808px;overflow:hidden}
body{position:relative;background:var(--white);font-family:"Open Sans",Arial,sans-serif;color:var(--ink)}
.abs{position:absolute}
.heading{font-family:"Nunito",Arial,sans-serif;font-weight:800}
.lorem{font-size:11px;line-height:15px;color:var(--muted)}

/* header */
.site-header{left:0;top:0;width:1200px;height:66px;background:var(--white)}
.brand{left:48px;top:16px;display:flex;align-items:center;gap:8px}
.brand-mark{width:34px;height:34px;border:2px solid var(--navy);background:var(--white)}
.brand-name{font-family:"Nunito",sans-serif;font-weight:800;font-size:28px;color:var(--navy);line-height:1}
.main-nav{left:318px;top:26px;display:flex;gap:24px;font-size:11px;color:var(--ink);white-space:nowrap}
.main-nav .active{color:var(--cyan)}
.search-icon{left:982px;top:25px}
.phone-btn{left:1015px;top:14px;width:135px;height:42px;background:var(--cyan);color:var(--white);font-size:12px;font-weight:700;display:flex;align-items:center;justify-content:center;gap:6px}

/* hero */
.hero{left:0;top:66px;width:1200px;height:590px;background:linear-gradient(180deg,#3d4a36 0%,#2f5c5a 40%,#1e6f7e 60%,#3a4a35 100%)}
.hero-title{left:0;top:272px;width:1200px;text-align:center;color:var(--white);font-size:48px;line-height:56px;font-weight:700}
.hero-title span{color:var(--cyan)}
.btn{display:flex;align-items:center;justify-content:center;font-size:12px;font-weight:600}
.btn-solid{background:var(--cyan);color:var(--white)}
.btn-outline{background:var(--white);color:var(--cyan);border:1px solid var(--cyan)}
.hero-cta{left:532px;top:424px;width:136px;height:40px}
.play{left:52px;top:484px;width:90px;height:90px;border-radius:50%;background:rgba(255,255,255,.3);display:flex;align-items:center;justify-content:center}
.play i{width:54px;height:54px;border-radius:50%;background:var(--white);display:flex;align-items:center;justify-content:center}

.section-title{color:var(--cyan-deep);font-size:34px}

/* services accordion */
.services{left:48px;top:756px;width:1100px;height:590px}
.svc{position:absolute;top:0;height:590px;background:var(--panel);box-shadow:-6px 0 10px rgba(0,0,0,.12);padding:24px 14px 0;overflow:hidden}
.svc h3{font-family:"Nunito",sans-serif;font-weight:700;font-size:18px;line-height:22px;color:var(--ink);white-space:nowrap;margin-bottom:12px}
.svc .lorem{width:150px}
.svc .photo{position:absolute;left:0;bottom:12px;width:100%;height:290px;padding:0 12px}
.svc .photo div{width:100%;height:100%}
.svc.is-open{background:var(--cyan)}
.svc.is-open h3,.svc.is-open .lorem{color:var(--white)}

/* pool types */
.pool-card{top:1413px;width:346px;height:342px;border:4px solid #7fd6f2;overflow:hidden}
.pool-card .label{position:absolute;left:36px;right:36px;top:146px;height:52px;background:var(--white);display:flex;align-items:center;justify-content:center;font-family:"Nunito",sans-serif;font-weight:700;font-size:18px;color:var(--ink)}
.pool-card .detail{position:absolute;left:30px;top:50px;width:305px;height:260px;background:rgba(255,255,255,.88);text-align:center;padding:36px 24px 0}
.detail h4{font-family:"Nunito",sans-serif;font-weight:700;font-size:18px;margin-bottom:10px}
.read-more{display:inline-flex;align-items:center;gap:8px;font-size:11px;font-weight:600;color:var(--ink)}
.arrow-box{width:18px;height:18px;border:1px solid var(--ink);display:inline-flex;align-items:center;justify-content:center}

/* projects */
.dark-band{left:0;width:1200px;background:var(--charcoal)}
.card{background:var(--white);box-shadow:0 4px 18px rgba(0,0,0,.12);text-align:center}
.card .photo{width:100%;height:188px}
.project{top:1872px;width:267px;height:390px}
.project h4{font-family:"Nunito",sans-serif;font-weight:700;font-size:18px;margin:24px 0 14px}
.project .lorem{padding:0 26px;margin-bottom:22px}
.slider-arrow{width:36px;height:36px;border:1px solid #c7ccd2;background:var(--white);display:flex;align-items:center;justify-content:center}

/* review */
.review-label{left:0;top:2288px;width:1200px;text-align:center;color:var(--cyan);font-size:12px;font-weight:700;letter-spacing:2px}
.stars{left:0;top:2292px;width:1200px;display:flex;justify-content:center;gap:4px}
.quote{left:0;top:2318px;width:1200px;text-align:center;color:var(--white);font-family:"Nunito",sans-serif;font-weight:600;font-size:33px;line-height:42px}
.quote-name{left:0;top:2446px;width:1200px;text-align:center;color:var(--white);font-size:17px}
.quote-role{left:0;top:2476px;width:1200px;text-align:center;color:var(--white);font-size:11px}

/* stats */
.stats-box{left:183px;top:2657px;width:834px;height:146px;border:1px dashed #7badd7;border-top:none}
.stat{top:2630px;width:240px;text-align:center;background:var(--white)}
.stat b{display:block;font-family:"Nunito",sans-serif;font-weight:800;font-size:46px;color:var(--cyan-deep);line-height:56px}
.stat span{font-size:15px;color:var(--ink)}
.finance-note{left:0;top:2746px;width:1200px;text-align:center;font-size:12px;color:var(--muted)}
.quote-btn{left:460px;top:2780px;width:136px;height:42px}
.finance-btn{left:604px;top:2780px;width:136px;height:42px}

/* news */
.news{top:3014px;width:267px;height:392px;text-align:left}
.news h4{font-family:"Nunito",sans-serif;font-weight:700;font-size:14px;line-height:18px;color:var(--navy);padding:20px 18px 10px}
.news .lorem{padding:0 18px}
.news .meta{position:absolute;left:18px;right:18px;bottom:22px;display:flex;justify-content:space-between;align-items:center}
.news .date{font-size:9px;color:#b6bac0}
.news-btn{left:532px;top:3450px;width:136px;height:42px}

/* gallery */
.shot{overflow:hidden}
.tag{position:absolute;left:14px;top:14px;padding:5px 12px;background:var(--white);color:var(--navy);font-size:11px;font-weight:700;letter-spacing:1px}
.tag.after{background:var(--cyan);color:var(--white)}

/* cta */
.cta-title{left:0;top:4262px;width:1200px;text-align:center;color:var(--navy);font-size:48px;line-height:56px}
.cta-btn{left:502px;top:4382px;width:196px;height:42px}

/* footer */
.site-footer{left:0;top:4471px;width:1200px;height:337px;background:var(--footer);color:var(--white)}
.site-footer .brand-mark{border-color:var(--white)}
.site-footer .brand-name{color:var(--white);font-size:36px}
.foot-text{left:48px;top:126px;width:300px;font-size:10px;line-height:16px;color:#dfe5ee}
.foot-head{font-family:"Nunito",sans-serif;font-weight:700;font-size:17px;color:#c9d3e2;letter-spacing:.5px}
.foot-links{list-style:none;font-size:10px;line-height:30px;margin-top:6px}
.contact-row{display:flex;align-items:flex-start;gap:14px;font-size:11px;line-height:16px;margin-bottom:20px}
.social{display:flex;gap:22px;margin-top:16px}
.social i{width:22px;height:22px;border-radius:50%;background:var(--white)}
.foot-rule{left:0;top:266px;width:1200px;height:1px;background:rgba(255,255,255,.15)}
.copyright{left:0;top:300px;width:1200px;text-align:center;font-size:9px;color:#dfe5ee}
</style>
</head>
<body>

<header class="abs site-header">
  <div class="abs brand"><div class="brand-mark"></div><div class="brand-name">Tidewell</div></div>
  <nav class="abs main-nav">
    <span class="active">• Home</span><span>New Builds ▾</span><span>Renovations ▾</span><span>Design ▾</span><span>Gallery</span><span>Financing</span><span>Reviews</span><span>Contact</span>
  </nav>
  <svg class="abs search-icon" width="16" height="16" viewBox="0 0 16 16"><circle cx="7" cy="7" r="5" fill="none" stroke="#555" stroke-width="1.5"/><line x1="11" y1="11" x2="15" y2="15" stroke="#555" stroke-width="1.5"/></svg>
  <div class="abs phone-btn">
    <svg width="12" height="12" viewBox="0 0 24 24"><path d="M6.6 10.8a15 15 0 006.6 6.6l2.2-2.2a1 1 0 011-.25 11.4 11.4 0 003.6.57 1 1 0 011 1V20a1 1 0 01-1 1A17 17 0 013 4a1 1 0 011-1h3.5a1 1 0 011 1c0 1.25.2 2.45.57 3.57a1 1 0 01-.25 1z" fill="#fff"/></svg>
    850-555-WAVE
  </div>
</header>

<section class="abs hero" role="img" aria-label="Aerial view of a backyard lap pool surrounded by palms and lawn"></section>
<h1 class="abs hero-title heading">Turning Backyards into<br>Oasis of <span>Relaxation</span></h1>
<a class="abs btn btn-solid hero-cta">Contact Us Now</a>
<div class="abs play"><i><svg width="22" height="22" viewBox="0 0 22 22"><circle cx="11" cy="11" r="10" fill="#1aa6d9"/><path d="M8 6l8 5-8 5z" fill="#fff"/></svg></i></div>
<svg class="abs" style="left:0;top:612px" width="1200" height="46" viewBox="0 0 1200 46" preserveAspectRatio="none"><path d="M0 22 L40 28 L80 20 L130 30 L170 24 L220 32 L270 26 L320 34 L370 28 L420 36 L470 30 L520 38 L570 32 L620 36 L670 28 L720 34 L770 26 L820 32 L870 22 L920 30 L970 20 L1020 26 L1070 14 L1120 20 L1160 8 L1200 12 L1200 46 L0 46Z" fill="#fff"/></svg>

<h2 class="abs section-title heading" style="left:48px;top:694px">Our Services</h2>

<div class="abs services">
  <div class="svc" style="left:0;width:170px;z-index:1">
    <h3>Pool Design</h3>
    <p class="lorem">Lorem ipsum dolor sit amet, adipiscing elit. Nunc tincidunt porttitor massa ornare vitae diam.</p>
    <div class="photo"><div role="img" aria-label="Hand sketching a pool plan on paper" style="background:linear-gradient(160deg,#e9eef2,#b9c2cc)"></div></div>
  </div>
  <div class="svc" style="left:155px;width:170px;z-index:2">
    <h3>Pool Construction</h3>
    <p class="lorem">Lorem ipsum dolor sit amet, adipiscing elit. Nunc tincidunt porttitor massa ornare vitae diam.</p>
    <div class="photo"><div role="img" aria-label="Crew spraying concrete for a pool shell" style="background:linear-gradient(160deg,#b9ad9a,#7f7467)"></div></div>
  </div>
  <div class="svc" style="left:317px;width:170px;z-index:3">
    <h3>Tile and Coping<br>Installation</h3>
    <p class="lorem">Lorem ipsum dolor sit amet, adipiscing elit. Nunc tincidunt porttitor massa ornare vitae diam.</p>
    <div class="photo"><div role="img" aria-label="Worker setting out levels with a laser tripod" style="background:linear-gradient(160deg,#c9cfc6,#6f7b76)"></div></div>
  </div>
  <div class="svc" style="left:479px;width:170px;z-index:4">
    <h3>Deck and Patio<br>Design</h3>
    <p class="lorem">Lorem ipsum dolor sit amet, adipiscing elit. Nunc tincidunt porttitor massa ornare vitae diam.</p>
    <div class="photo"><div role="img" aria-label="Pool deck with loungers and umbrellas" style="background:linear-gradient(160deg,#e8e1d6,#b5454e)"></div></div>
  </div>
  <div class="svc is-open" style="left:639px;width:461px;z-index:5;padding:24px 18px 0">
    <h3>Pool Finishes</h3>
    <p class="lorem" style="width:260px">Lorem ipsum dolor sit amet, consectetur adipiscing elit. Nunc tincidunt leo tortor, id porttitor massa ornare vitae. Etiam in convallis diam, vestibulum fermentum libero. Mauris quis</p>
    <div class="photo" style="padding:0 16px"><div role="img" aria-label="Finished turquoise pool with step entry and garden" style="background:linear-gradient(180deg,#5f8c4c 0%,#4fc3e6 45%,#2aa7d6 100%)"></div></div>
  </div>
</div>

<div class="abs pool-card" style="left:48px" role="img" aria-label="Concrete pool edge at sunset">
  <div style="width:100%;height:100%;background:linear-gradient(160deg,#4b7a8b,#c99a5c)"></div>
  <div class="detail">
    <h4>Concrete Pools</h4>
    <p class="lorem" style="color:#6c7078">Lorem ipsum dolor sit amet, consectetur adipiscing elit, sed do eiusmod tempor incididunt ut labore et dolore magna aliqua. Quis ipsum suspendisse ultrices gravida. Risus commodo viverra maecenas accumsan lacus vel facilisis.</p>
    <p style="margin-top:14px"><span class="read-more">Read More <span class="arrow-box"><svg width="9" height="9" viewBox="0 0 9 9"><path d="M1 8L8 1M3 1h5v5" stroke="#333" fill="none"/></svg></span></span></p>
  </div>
</div>
<div class="abs pool-card" style="left:425px" role="img" aria-label="Tiled pool with chrome ladder">
  <div style="width:100%;height:100%;background:linear-gradient(180deg,#5b9d4d 0%,#1f77c9 35%,#3a8fd8 70%,#e79a8e 100%)"></div>
  <div class="label">Vinyl Liner Pools</div>
</div>
<div class="abs pool-card" style="left:802px" role="img" aria-label="Fiberglass pool with curved steps">
  <div style="width:100%;height:100%;background:linear-gradient(160deg,#5aa3d8,#1d6fb8)"></div>
  <div class="label">Fiberglass Pools</div>
</div>

<h2 class="abs section-title heading" style="left:0;top:1802px;width:1200px;text-align:center">Our Projects</h2>

<div class="abs dark-band" style="top:2114px;height:470px"></div>
<svg class="abs" style="left:0;top:2548px" width="1200" height="40" viewBox="0 0 1200 40" preserveAspectRatio="none"><path d="M0 8 L60 14 L120 6 L180 16 L240 10 L300 18 L360 8 L420 16 L480 10 L540 20 L600 12 L660 18 L720 8 L780 16 L840 10 L900 20 L960 12 L1020 18 L1080 8 L1140 14 L1200 6 L1200 40 L0 40Z" fill="#fff"/></svg>

<div class="abs slider-arrow" style="left:48px;top:1951px"><svg width="14" height="10" viewBox="0 0 14 10"><path d="M13 5H1M5 1L1 5l4 4" stroke="#888" fill="none"/></svg></div>
<div class="abs slider-arrow" style="left:1114px;top:1951px"><svg width="14" height="10" viewBox="0 0 14 10"><path d="M1 5h12M9 1l4 4-4 4" stroke="#1aa6d9" fill="none"/></svg></div>

<article class="abs card project" style="left:183px">
  <div class="photo" role="img" aria-label="Pool edge with potted palm" style="background:linear-gradient(160deg,#7fd3d9,#3aa9b0)"></div>
  <h4>Project 1</h4>
  <p class="lorem">Lorem ipsum dolor sit amet, consectetur adipiscing elit, sed do eiusmod tempor incididunt ut labore et dolore magna aliqua. Quis ipsum suspendisse ultrices gravida.</p>
  <span class="read-more">View Details <span class="arrow-box"><svg width="9" height="9" viewBox="0 0 9 9"><path d="M1 8L8 1M3 1h5v5" stroke="#333" fill="none"/></svg></span></span>
</article>
<article class="abs card project" style="left:466px">
  <div class="photo" role="img" aria-label="Resort pool with palms at sunset" style="background:linear-gradient(180deg,#e8b573 0%,#6c7f4a 50%,#4aa9c9 100%)"></div>
  <h4>Project 2</h4>
  <p class="lorem">Lorem ipsum dolor sit amet, consectetur adipiscing elit, sed do eiusmod tempor incididunt ut labore et dolore magna aliqua. Quis ipsum suspendisse ultrices gravida.</p>
  <span class="read-more">View Details <span class="arrow-box"><svg width="9" height="9" viewBox="0 0 9 9"><path d="M1 8L8 1M3 1h5v5" stroke="#333" fill="none"/></svg></span></span>
</article>
<article class="abs card project" style="left:748px">
  <div class="photo" role="img" aria-label="Lap pool beside a villa" style="background:linear-gradient(180deg,#a9c3d6 0%,#5d7a55 50%,#2f8fc7 100%)"></div>
  <h4>Project 3</h4>
  <p class="lorem">Lorem ipsum dolor sit amet, consectetur adipiscing elit, sed do eiusmod tempor incididunt ut labore et dolore magna aliqua. Quis ipsum suspendisse ultrices gravida.</p>
  <span class="read-more">View Details <span class="arrow-box"><svg width="9" height="9" viewBox="0 0 9 9"><path d="M1 8L8 1M3 1h5v5" stroke="#333" fill="none"/></svg></span></span>
</article>

<section aria-label="Customer reviews">
  <p class="abs review-label" style="top:2272px">CUSTOMER REVIEWS</p>
  <div class="abs stars" aria-label="Five star rating">
    <svg width="14" height="14" viewBox="0 0 24 24"><path d="M12 2l3 7h7l-5.5 4.5 2 7.5-6.5-4.5L5.5 21l2-7.5L2 9h7z" fill="#f5b82e"/></svg>
    <svg width="14" height="14" viewBox="0 0 24 24"><path d="M12 2l3 7h7l-5.5 4.5 2 7.5-6.5-4.5L5.5 21l2-7.5L2 9h7z" fill="#f5b82e"/></svg>
    <svg width="14" height="14" viewBox="0 0 24 24"><path d="M12 2l3 7h7l-5.5 4.5 2 7.5-6.5-4.5L5.5 21l2-7.5L2 9h7z" fill="#f5b82e"/></svg>
    <svg width="14" height="14" viewBox="0 0 24 24"><path d="M12 2l3 7h7l-5.5 4.5 2 7.5-6.5-4.5L5.5 21l2-7.5L2 9h7z" fill="#f5b82e"/></svg>
    <svg width="14" height="14" viewBox="0 0 24 24"><path d="M12 2l3 7h7l-5.5 4.5 2 7.5-6.5-4.5L5.5 21l2-7.5L2 9h7z" fill="#f5b82e"/></svg>
  </div>
  <p class="abs quote" style="top:2326px">A pool is like a blank canvas, the<br>possibilities are endless.</p>
  <p class="abs quote-name">Aldo Rennick</p>
  <p class="abs quote-role">Concrete pool renovation client, Cedarbrook</p>
</section>

<div class="abs stats-box"></div>
<div class="abs" style="left:183px;top:2657px;width:40px;border-top:1px dashed #7badd7"></div>
<div class="abs" style="left:977px;top:2657px;width:40px;border-top:1px dashed #7badd7"></div>
<div class="abs stat" style="left:188px"><b>5K+</b><span>Happy Clients</span></div>
<div class="abs stat" style="left:480px"><b>5Years+</b><span>Successful Years</span></div>
<div class="abs stat" style="left:753px"><b>500+</b><span>Pools Built</span></div>
<p class="abs finance-note">Flexible financing available for new builds and renovations</p>
<a class="abs btn btn-outline quote-btn">Get a Quote</a>
<a class="abs btn btn-solid finance-btn">Financing Options</a>

<div class="abs dark-band" style="top:2880px;height:690px"></div>
<svg class="abs" style="left:0;top:2852px" width="1200" height="40" viewBox="0 0 1200 40" preserveAspectRatio="none"><path d="M0 36 L80 30 L160 34 L240 26 L320 32 L400 22 L480 28 L560 18 L640 24 L720 16 L800 22 L880 12 L960 18 L1040 8 L1120 14 L1200 4 L1200 40 L0 40Z" fill="#3b4047"/></svg>
<svg class="abs" style="left:0;top:3556px" width="1200" height="30" viewBox="0 0 1200 30" preserveAspectRatio="none"><path d="M0 0 L1200 0 L1200 10 Q900 24 600 16 Q300 8 0 22Z" fill="#3b4047"/></svg>

<h2 class="abs section-title heading" style="left:0;top:2940px;width:1200px;text-align:center;color:#fff">News &amp; Articles</h2>
<div class="abs slider-arrow" style="left:48px;top:3180px"><svg width="14" height="10" viewBox="0 0 14 10"><path d="M13 5H1M5 1L1 5l4 4" stroke="#888" fill="none"/></svg></div>
<div class="abs slider-arrow" style="left:1114px;top:3180px"><svg width="14" height="10" viewBox="0 0 14 10"><path d="M1 5h12M9 1l4 4-4 4" stroke="#1aa6d9" fill="none"/></svg></div>

<article class="abs card news" style="left:183px">
  <div class="photo" role="img" aria-label="Family playing in a seaside pool" style="height:168px;background:linear-gradient(180deg,#9cc8e3 0%,#2a9ad0 100%)"></div>
  <h4>A Family's Journey to Their Dream Concrete Pool</h4>
  <p class="lorem">Lorem ipsum dolor sit amet, consectetur adipiscing elit, sed do eiusmod tempor incididunt ut labore et dolore magna aliqua. Quis ipsum suspendisse ultrices gravida.</p>
  <div class="meta"><span class="read-more">Read More <span class="arrow-box"><svg width="9" height="9" viewBox="0 0 9 9"><path d="M1 8L8 1M3 1h5v5" stroke="#333" fill="none"/></svg></span></span><span class="date">05/09/2023</span></div>
</article>
<article class="abs card news" style="left:466px">
  <div class="photo" role="img" aria-label="Crew applying concrete to a pool shell" style="height:168px;background:linear-gradient(160deg,#b9ad9a,#7f7467)"></div>
  <h4>Eco-Friendly Approaches to Concrete Pool Construction</h4>
  <p class="lorem">Lorem ipsum dolor sit amet, consectetur adipiscing elit, sed do eiusmod tempor incididunt ut labore et dolore magna aliqua. Quis ipsum suspendisse ultrices gravida.</p>
  <div class="meta"><span class="read-more">Read More <span class="arrow-box"><svg width="9" height="9" viewBox="0 0 9 9"><path d="M1 8L8 1M3 1h5v5" stroke="#333" fill="none"/></svg></span></span><span class="date">05/09/2023</span></div>
</article>
<article class="abs card news" style="left:748px">
  <div class="photo" role="img" aria-label="Resort pool with palm trees at dusk" style="height:168px;background:linear-gradient(180deg,#e8b573 0%,#6c7f4a 50%,#4aa9c9 100%)"></div>
  <h4>Transforming a Backyard with a Concrete Pool Renovation</h4>
  <p class="lorem">Lorem ipsum dolor sit amet, consectetur adipiscing elit, sed do eiusmod tempor incididunt ut labore et dolore magna aliqua. Quis ipsum suspendisse ultrices gravida.</p>
  <div class="meta"><span class="read-more">Read More <span class="arrow-box"><svg width="9" height="9" viewBox="0 0 9 9"><path d="M1 8L8 1M3 1h5v5" stroke="#333" fill="none"/></svg></span></span><span class="date">05/09/2023</span></div>
</article>
<a class="abs btn btn-outline news-btn">View All News</a>

<section aria-label="Gallery and before and after">
  <div class="abs shot" style="left:48px;top:3639px;width:254px;height:272px;background:linear-gradient(180deg,#c9c3b4 0%,#8a8170 50%,#6b7d86 100%)" role="img" aria-label="Worn pool before renovation"><span class="tag">BEFORE</span></div>
  <div class="abs shot" style="left:325px;top:3639px;width:254px;height:272px;background:linear-gradient(180deg,#8fc7ec 0%,#e2e2da 40%,#1d8fd0 100%)" role="img" aria-label="Same pool after renovation with new finish"><span class="tag after">AFTER</span></div>
  <div class="abs shot" style="left:601px;top:3639px;width:547px;height:272px;background:linear-gradient(180deg,#c9d7cf 0%,#6f8f5a 35%,#3cb2de 100%)" role="img" aria-label="Friends jumping into a new concrete pool"><span class="tag">GALLERY</span></div>
  <div class="abs shot" style="left:48px;top:3935px;width:531px;height:273px;background:linear-gradient(180deg,#dfe6e8 0%,#6d8b5a 45%,#1e8fbf 100%)" role="img" aria-label="Pool with water jets and umbrellas"><span class="tag">GALLERY</span></div>
  <div class="abs shot" style="left:601px;top:3935px;width:263px;height:273px;background:linear-gradient(180deg,#b9b2a2 0%,#8f8877 50%,#5d7480 100%)" role="img" aria-label="Backyard pool before remodeling"><span class="tag">BEFORE</span></div>
  <div class="abs shot" style="left:886px;top:3935px;width:262px;height:273px;background:linear-gradient(180deg,#cfe3ef 0%,#3fa5c8 55%,#2c5e7a 100%)" role="img" aria-label="Same backyard after remodeling with infinity edge"><span class="tag after">AFTER</span></div>
</section>

<h2 class="abs cta-title heading">Let's Make Your Pool<br>Dream a Reality</h2>
<a class="abs btn btn-solid cta-btn">Request a Free Quote</a>

<footer class="abs site-footer">
  <div class="abs brand" style="left:48px;top:50px"><div class="brand-mark" style="width:46px;height:46px"></div><div class="brand-name">Tidewell</div></div>
  <p class="abs foot-text">Lorem ipsum dolor sit amet, consectetur adipiscing elit, sed do eiusmod tempor incididunt ut labore et dolore magna aliqua. Quis ipsum suspendisse ultrices gravida. Risus commodo viverra maecenas accumsan lacus vel facilisis.</p>

  <div class="abs" style="left:560px;top:50px">
    <h5 class="foot-head">QUICK LINKS</h5>
    <ul class="foot-links"><li>NEW BUILDS</li><li>RENOVATIONS</li><li>FINANCING</li><li>GALLERY</li><li>REVIEWS</li><li>CONTACT US</li></ul>
  </div>

  <div class="abs" style="left:741px;top:50px">
    <h5 class="foot-head" style="margin-bottom:22px">CONTACT US</h5>
    <div class="contact-row"><svg width="14" height="14" viewBox="0 0 24 24"><path d="M6.6 10.8a15 15 0 006.6 6.6l2.2-2.2a1 1 0 011-.25 11.4 11.4 0 003.6.57 1 1 0 011 1V20a1 1 0 01-1 1A17 17 0 013 4a1 1 0 011-1h3.5a1 1 0 011 1c0 1.25.2 2.45.57 3.57a1 1 0 01-.25 1z" fill="#fff"/></svg>(850) 555-0142</div>
    <div class="contact-row"><svg width="14" height="12" viewBox="0 0 14 12"><rect x="0.5" y="0.5" width="13" height="11" fill="#fff"/><path d="M1 1l6 5 6-5" stroke="#3e4e68" fill="none"/></svg>hello@tidewellpools.com</div>
    <div class="contact-row"><svg width="14" height="18" viewBox="0 0 14 18"><path d="M7 0a7 7 0 00-7 7c0 5 7 11 7 11s7-6 7-11a7 7 0 00-7-7z" fill="#fff"/><circle cx="7" cy="7" r="2.5" fill="#3e4e68"/></svg>1480 Marlow Ln<br>Cedarbrook, FL 32390</div>
  </div>

  <div class="abs" style="left:955px;top:50px;width:1px;height:170px;background:rgba(255,255,255,.25)"></div>

  <div class="abs" style="left:987px;top:50px">
    <h5 class="foot-head">KEEP IN TOUCH</h5>
    <p style="font-size:11px;margin-top:10px">Follow us to stay up to date</p>
    <div class="social" aria-label="Social media links"><i></i><i></i><i></i><i></i></div>
  </div>

  <div class="abs foot-rule"></div>
  <p class="abs copyright">Copyright © 2019 Tidewell. All Right Reserved</p>
</footer>

</body>
</html>
```